Design 5 colour schemes for one web page

We are looking for 5 different colour schemes for our product template to create different kinds of colour tone for our web page, it doesn't need to be restructure the layout, just need to provide different color solution.

Please refer to the attached images and take note of the following when you’re working on the design:
(1) Please precisely reproduce the layout. Cannot remove or delete any wordings, components or column shown in the images.
(2) Okay to revise icons, background color or text style as you prefer. But cannot move/delete them.
(3) Provide PSD source files with good layer management. HTML/CSS are not required.
(4) Make reasonable and professional design.

After completion, please send back:
(1) 5 images with 5 different colour schemes.
(2) Related PSD files.

Industry/Entity Type

Management

Number of Pages Required

1 page

Font styles to use
Serif
Sans Serif

Requirements
Must have
• (1) 5 images for the colour schemes.
• (2) 5 PSD source files with good layer management.
Nice to have
• (1) Explanation about your design of the colour schemes.
Should not have
• (1) HTML/CSS code are not required.

```html
<!DOCTYPE html>
<html lang="en">
<head>
<meta charset="utf-8">
<title>Sports – Today Live</title>
<link href="https://fonts.googleapis.com/css2?family=Open+Sans:wght@400;600;700&display=swap" rel="stylesheet">
<style>
:root{
  --topbar:#173a2b;
  --header-a:#1b6a45;
  --header-b:#2f9a62;
  --navbar:#12271d;
  --panel-dark:#14291f;
  --col-head:#25704b;
  --col-line:#6fa98a;
  --side-mid:#25704b;
  --accent:#f2a024;
  --row-light:#f8f8f5;
  --row-alt:#dcefe2;
  --line:#a3b5aa;
  --divider:#4f6b5c;
  --line-odds:#1e8f68;
  --red:#d3262b;
  --ink:#1c1c1c;
  --white:#ffffff;
  --badge:#e0592b;
  --fav-up:#0f5a3a;
  --icon-grey:#5d6a63;
}
*{box-sizing:border-box;margin:0;padding:0}
html,body{width:1200px;height:1155px;overflow:hidden;background:var(--white)}
body{font-family:"Open Sans",Arial,sans-serif;color:var(--ink)}
.stage{width:1070px;height:1030px;transform:scale(1.1215);transform-origin:0 0;position:relative}
.defs{position:absolute;width:0;height:0}

/* top bar */
.topbar{height:34px;background:var(--topbar);display:flex;align-items:center;padding:0 49px;color:var(--white);font-size:12.5px}
.topbar nav{display:flex;gap:13px;align-items:center}
.topbar .badge{background:var(--badge);font-size:11px;padding:0 5px;border-radius:2px;margin-left:-6px;line-height:17px}
.account{margin-left:auto;display:flex;align-items:center;gap:8px}
.balance{border:1px solid var(--white);padding:0 6px;height:19px;display:flex;align-items:center;gap:5px;font-size:12px}
.signout{border:1px solid var(--white);background:var(--navbar);padding:0 9px;height:20px;line-height:18px;margin-left:4px}

/* brand header */
.brandbar{position:absolute;left:38px;top:34px;width:992px;height:73px;background:linear-gradient(180deg,var(--header-b),var(--header-a))}
.brand-name{position:absolute;left:24px;top:2px;font-size:58px;color:var(--white);letter-spacing:1px;line-height:64px}
.tab-sports{position:absolute;left:280px;top:23px;width:84px;height:50px;background:var(--white);font-size:14px;text-align:center;padding-top:12px}
.results-link{position:absolute;right:6px;top:9px;font-size:10px;color:var(--white);display:flex;gap:5px;align-items:center}
.navbar{position:absolute;left:38px;top:107px;width:992px;height:24px;background:var(--navbar);color:var(--white);font-size:13px;display:flex;align-items:center}
.navbar .lang{display:flex;gap:6px;align-items:center;padding:0 10px 0 3px;border-right:1px solid var(--divider);height:100%}
.navbar .clock{padding-left:10px}
.tools{margin-left:auto;display:flex;height:100%;font-size:10.5px}
.tools span{border-left:1px solid var(--divider);padding:0 8px;display:flex;align-items:center;gap:3px}

/* sidebar */
.sidebar{position:absolute;left:38px;top:138px;width:174px}
.panel-head{background:var(--panel-dark);color:var(--white);font-size:12px;text-align:center;height:35px;line-height:37px;border-radius:5px 5px 0 0}
.fav-body{background:var(--side-mid);height:64px;padding:8px 9px}
.fav-hint{border:1px dashed #cfe3d7;color:var(--white);font-size:10.5px;text-align:center;line-height:14px;padding:9px 2px}
.tabs{display:flex;margin-top:7px;height:24px;font-size:12px}
.tabs div{flex:1;text-align:center;line-height:24px}
.tab-on{background:var(--panel-dark);color:var(--white);border-radius:5px 0 0 0}
.tab-off{background:var(--accent);color:var(--ink);border-radius:0 5px 0 0}
.sport-list{background:var(--panel-dark);padding:5px 0 3px;list-style:none}
.sport-list li{display:flex;align-items:center;height:23.15px;color:var(--white);font-size:12px;font-weight:600;padding:0 3px 0 6px;border-bottom:1px solid #284034;white-space:nowrap}
.sport-list li svg{width:20px;height:18px;margin-right:7px;flex:none}
.sport-list li b{margin-left:auto;font-weight:600;padding-left:4px}
.tabs.slip{margin-top:12px;height:27px}
.tabs.slip div{line-height:27px}
.parlay-count{display:inline-block;border:1px solid var(--ink);font-size:10px;line-height:11px;padding:0 2px;margin-left:14px}
.mybets{margin-top:15px}
.mybets-body{background:var(--side-mid);padding:7px 9px 11px;text-align:center;color:var(--white)}
.refresh{font-size:13px;display:flex;justify-content:center;gap:6px;align-items:center;margin-bottom:6px}
.no-bets{background:var(--accent);color:var(--ink);font-size:12px;height:23px;line-height:22px}
.view-all{background:var(--panel-dark);color:var(--white);font-size:12px;text-align:center;height:21px;line-height:21px}

/* odds boards */
.board{position:absolute;left:220px;width:810px}
.board-title{background:var(--panel-dark);color:var(--white);height:35px;display:flex;align-items:center;padding:0 8px;font-size:12.5px;font-weight:600;position:relative}
.board-title .title{display:flex;gap:6px;align-items:center}
.board-title .count{position:absolute;left:392px;display:flex;gap:3px;align-items:center}
.board-title .league-pick{margin-left:auto;display:flex;gap:6px;align-items:center}
.grid{display:grid}
.col-head{grid-template-columns:60px 177px 284px 246px 43px;background:var(--col-head);color:var(--white);height:35px}
.col-head>div{border-right:1px solid var(--col-line);display:flex;align-items:center;justify-content:center;font-size:12px}
.col-head .ft{display:grid;grid-template-columns:37px 86px 115px 46px;grid-template-rows:18px 17px}
.col-head .ft2{display:grid;grid-template-columns:119px 78px 49px;grid-template-rows:18px 17px}
.ft>div,.ft2>div{display:flex;align-items:center;justify-content:center;font-size:11px}
.ft .top,.ft2 .top{grid-column:1/-1;border-bottom:1px solid var(--col-line);font-size:12px}
.ft .sub,.ft2 .sub{border-right:1px solid var(--col-line)}
.ft .sub:last-child,.ft2 .sub:last-child{border-right:0}
.col-head .more{border-right:0;font-size:11.5px}
.league{background:var(--panel-dark);color:var(--white);height:18px;font-size:11.5px;display:flex;align-items:center;padding-left:63px;position:relative}
.league .star{margin-right:3px}
.league .reload{position:absolute;right:8px;top:3px}
.match{grid-template-columns:23px 37px 177px 37px 86px 115px 46px 246px 43px;height:43px;border-bottom:1px solid var(--line);background:var(--row-light);font-size:12px}
.match.alt{background:var(--row-alt)}
.match.short{height:31px}
.match>div{position:relative}
.match .c-stat,.match .c-time,.match .c-event,.match .c-1x2,.match .c-ft2{border-right:1px solid var(--divider)}
.c-stat{display:flex;justify-content:center;padding-top:10px}
.c-time{font-size:9px;color:#333;line-height:11px;padding:7px 0 0 3px}
.c-time em{color:var(--red);font-style:italic;font-size:11.5px;display:block;line-height:14px}
.c-event{display:flex;padding:2px 0 0 3px}
.c-event svg{margin-top:7px;margin-right:3px;flex:none}
.teams{line-height:12.5px;font-weight:600;white-space:nowrap}
.teams .home,.teams .draw{color:#2b2b2b}
.teams .away{color:var(--red)}
.line-val{position:absolute;color:var(--line-odds);font-size:10.5px}
.c-hdp .line-val{left:8px;top:16px}
.c-ou .line-val{left:8px;top:1px}
.odds{position:absolute;top:2px;text-align:right;line-height:13px;font-weight:600}
.c-hdp .odds{right:3px}
.c-ou .odds{right:4px}
.ab{position:absolute;left:62px;top:5px;font-size:10.5px;line-height:13px}
.neg{color:var(--red)}
.pos{color:var(--ink)}
.up{color:var(--fav-up)}
.c-more{display:flex;align-items:center;padding-left:7px;color:#333}
.c-more svg{margin-right:1px}

/* footer */
.footer{position:absolute;top:992px;left:353px;font-size:12px;color:#777;display:flex;gap:9px}
.footer i{font-style:normal;color:#999}
</style>
</head>
<body>
<svg class="defs" aria-hidden="true">
  <defs>
    <symbol id="i-reload" viewBox="0 0 12 12"><path d="M10 6a4 4 0 1 1-1.2-2.8" fill="none" stroke="currentColor" stroke-width="1.4"/><path d="M9 1v3H6" fill="none" stroke="currentColor" stroke-width="1.4"/></symbol>
    <symbol id="i-star" viewBox="0 0 12 12"><path d="M6 0l1.8 3.9 4.2.4-3.2 2.8.9 4.1L6 9.1 2.3 11.2l.9-4.1L0 4.3l4.2-.4z" fill="#dfe6e1"/></symbol>
    <symbol id="i-star-o" viewBox="0 0 12 12"><path d="M6 .8l1.6 3.4 3.7.4-2.8 2.5.8 3.6L6 8.9l-3.3 1.8.8-3.6L.7 4.6l3.7-.4z" fill="none" stroke="#6f7a73"/></symbol>
    <symbol id="i-stat" viewBox="0 0 12 12"><rect width="12" height="12" rx="2" fill="#5d6a63"/><path d="M3 9V6M6 9V3M9 9V5" stroke="#fff" stroke-width="1.4"/></symbol>
    <symbol id="i-updown" viewBox="0 0 8 14"><path d="M4 0l4 6H0zM4 14L0 8h8z" fill="#555"/></symbol>
  </defs>
</svg>
<div class="stage">

  <header class="topbar">
    <nav>
      <span>My Bets</span><span>Statement</span><span>Preference</span><span>Announcements</span><span class="badge">99+</span>
    </nav>
    <div class="account">
      <span>Hi, stwtg036</span>
      <span class="balance">
        <svg width="12" height="10" viewBox="0 0 12 10"><path d="M0 0l5 5-5 5zM6 0l5 5-5 5z" fill="#fff"/></svg>
        SD$&nbsp;&nbsp;10,072.00
        <svg width="11" height="11" style="color:#fff"><use href="#i-reload"/></svg>
      </span>
      <span class="signout">Sign Out</span>
    </div>
  </header>

  <div class="brandbar">
    <div class="brand-name">LOGO</div>
    <div class="tab-sports">Sports</div>
    <div class="results-link">
      <svg width="16" height="12" viewBox="0 0 16 12"><rect x="1" y="6" width="4" height="6" fill="#fff"/><rect x="6" y="1" width="4" height="11" fill="#fff"/><rect x="11" y="4" width="4" height="8" fill="#fff"/></svg>
      Results
    </div>
  </div>

  <div class="navbar">
    <div class="lang">
      <svg width="18" height="18" viewBox="0 0 18 18"><circle cx="9" cy="9" r="8" fill="none" stroke="#fff" stroke-width="1.2"/><ellipse cx="9" cy="9" rx="3.5" ry="8" fill="none" stroke="#fff"/><path d="M1 9h16M2.5 5h13M2.5 13h13" stroke="#fff"/></svg>
      English (Asia) ▾
    </div>
    <div class="clock">12/02/2013 15:53PM GMT+8</div>
    <div class="tools">
      <span>⊞ ▾</span><span>★ ▾</span><span>▤ ▾</span><span>MY ▾</span><span>◂</span><span>▭</span><span>Live</span>
    </div>
  </div>

  <aside class="sidebar">
    <div class="panel-head">My Fevourites</div>
    <div class="fav-body"><div class="fav-hint">Click 0 an event or league to add it to"My Fevourites".</div></div>

    <div class="tabs"><div class="tab-on">Sports</div><div class="tab-off">Markets</div></div>
    <ul class="sport-list">
      <li><svg viewBox="0 0 20 18"><circle cx="10" cy="9" r="7" fill="none" stroke="#fff" stroke-width="1.6"/><path d="M10 6l3 2-1 3.4H8L7 8z" fill="#fff"/></svg>Football<b>600</b></li>
      <li><svg viewBox="0 0 20 18"><circle cx="10" cy="9" r="7" fill="none" stroke="#fff" stroke-width="1.6"/><path d="M3 9h14M10 2v14M5 4c3 3 3 7 0 10M15 4c-3 3-3 7 0 10" fill="none" stroke="#fff" stroke-width="1.2"/></svg>Basketball<b>600</b></li>
      <li><svg viewBox="0 0 20 18"><circle cx="10" cy="9" r="7" fill="none" stroke="#fff" stroke-width="1.6"/><path d="M6 4c2 3 2 7 0 10M14 4c-2 3-2 7 0 10" fill="none" stroke="#fff" stroke-width="1.3" stroke-dasharray="1.5 1"/></svg>Baseball<b>600</b></li>
      <li><svg viewBox="0 0 20 18"><ellipse cx="12" cy="6" rx="5" ry="5" fill="none" stroke="#fff" stroke-width="1.6"/><path d="M8.5 9.5L3 16" stroke="#fff" stroke-width="2.4"/></svg>Tennis<b>600</b></li>
      <li><svg viewBox="0 0 20 18"><ellipse cx="10" cy="9" rx="8" ry="5" transform="rotate(-30 10 9)" fill="#fff"/><path d="M8 10l4-2" stroke="#14291f" stroke-width="1.4"/></svg>American Football<b>600</b></li>
      <li><svg viewBox="0 0 20 18"><path d="M6 2h8l-2.5 10h-3z" fill="none" stroke="#fff" stroke-width="1.5"/><circle cx="10" cy="14" r="2.6" fill="#fff"/></svg>Badminton<b>600</b></li>
      <li><svg viewBox="0 0 20 18"><path d="M5 6a5 4 0 0 1 10 0v5H5z" fill="#fff"/><rect x="5" y="12" width="10" height="4" rx="1" fill="#fff"/></svg>Boxing<b>600</b></li>
      <li><svg viewBox="0 0 20 18"><path d="M14 2l3 3-9 9-3-3z" fill="#fff"/><path d="M5 13l-3 3" stroke="#fff" stroke-width="2"/><circle cx="15" cy="14" r="2" fill="#fff"/></svg>Cricket<b>600</b></li>
      <li><svg viewBox="0 0 20 18"><circle cx="5" cy="12" r="3.6" fill="none" stroke="#fff" stroke-width="1.5"/><circle cx="15" cy="12" r="3.6" fill="none" stroke="#fff" stroke-width="1.5"/><path d="M5 12l4-6h4l2 6M9 6l1 6" fill="none" stroke="#fff" stroke-width="1.4"/></svg>Cycling<b>600</b></li>
      <li><svg viewBox="0 0 20 18"><circle cx="10" cy="9" r="7.5" fill="none" stroke="#fff" stroke-width="1.5"/><circle cx="10" cy="9" r="4.5" fill="none" stroke="#fff" stroke-width="1.5"/><circle cx="10" cy="9" r="1.6" fill="#fff"/></svg>Darts<b>600</b></li>
      <li><svg viewBox="0 0 20 18"><path d="M10 1l2.4 5.2 5.6.6-4.2 3.8 1.2 5.6L10 13.4 5 16.2l1.2-5.6L2 6.8l5.6-.6z" fill="#fff"/></svg>Entertainment<b>600</b></li>
      <li><svg viewBox="0 0 20 18"><path d="M8 2v14" stroke="#fff" stroke-width="1.6"/><path d="M8 2l8 3-8 3z" fill="#fff"/><ellipse cx="9" cy="16" rx="6" ry="1.5" fill="#fff"/></svg>Golf<b>600</b></li>
      <li><svg viewBox="0 0 20 18"><circle cx="10" cy="9" r="7" fill="#fff"/><path d="M4 6c4 2 8 2 12 0M4 12c4-2 8-2 12 0" fill="none" stroke="#14291f" stroke-width="1.2"/></svg>Handball<b>600</b></li>
      <li><svg viewBox="0 0 20 18"><path d="M14 1L8 14h-5" fill="none" stroke="#fff" stroke-width="2.2" stroke-linejoin="round"/><rect x="12" y="13" width="6" height="3" rx="1" fill="#fff"/></svg>Ice Hockey<b>600</b></li>
      <li><svg viewBox="0 0 20 18"><rect x="4" y="4" width="12" height="10" rx="3" fill="#fff"/><path d="M8 4v5M12 4v5" stroke="#14291f" stroke-width="1.2"/></svg>Mixed Martial Art<b>600</b></li>
      <li><svg viewBox="0 0 20 18"><circle cx="10" cy="9" r="7" fill="none" stroke="#fff" stroke-width="2"/><circle cx="10" cy="9" r="2" fill="#fff"/><path d="M10 2v14M3 9h14" stroke="#fff" stroke-width="1.2"/></svg>Miotor Sports<b>600</b></li>
      <li><svg viewBox="0 0 20 18"><circle cx="10" cy="9" r="7" fill="#fff"/><circle cx="10" cy="9" r="3.2" fill="#14291f"/><circle cx="10" cy="9" r="1.4" fill="#fff"/></svg>Pool/Snooker<b>600</b></li>
      <li><svg viewBox="0 0 20 18"><ellipse cx="10" cy="9" rx="8" ry="5.5" fill="none" stroke="#fff" stroke-width="1.6"/><path d="M6 9h8M8 7.5v3M10 7.5v3M12 7.5v3" stroke="#fff" stroke-width="1.1"/></svg>Rugby<b>600</b></li>
      <li><svg viewBox="0 0 20 18"><circle cx="10" cy="9" r="7" fill="none" stroke="#fff" stroke-width="1.6"/><path d="M10 2c-2 4-1 8 4 12M3.5 7c4 0 8 2 9 8M16.5 6c-4 2-8 3-12 6" fill="none" stroke="#fff" stroke-width="1.2"/></svg>Volleyball<b>600</b></li>
      <li><svg viewBox="0 0 20 18"><path d="M10 1v16M3 5l14 8M17 5L3 13" stroke="#fff" stroke-width="1.6"/><path d="M8 2.5l2 1.5 2-1.5M8 15.5l2-1.5 2 1.5" fill="none" stroke="#fff" stroke-width="1.2"/></svg>Winter Sports<b>600</b></li>
    </ul>

    <div class="tabs slip"><div class="tab-on">Ticket</div><div class="tab-off">Parlay<span class="parlay-count">0</span></div></div>

    <div class="mybets">
      <div class="panel-head">My Bets</div>
      <div class="mybets-body">
        <div class="refresh"><svg width="13" height="13" style="color:#fff"><use href="#i-reload"/></svg>Refresh</div>
        <div class="no-bets">No pending bets</div>
      </div>
      <div class="view-all">View All</div>
    </div>
  </aside>

  <section class="board" style="top:138px">
    <div class="board-title">
      <span class="title"><svg width="20" height="18" viewBox="0 0 20 18"><circle cx="12" cy="4" r="3" fill="#fff"/><path d="M4 16l5-6 4 2 3-3" stroke="#fff" stroke-width="2.4" fill="none"/></svg>Today - Live</span>
      <span class="count"><svg width="14" height="14" style="color:#fff"><use href="#i-reload"/></svg>38</span>
      <span class="league-pick"><svg width="14" height="14" viewBox="0 0 14 14"><path d="M3 1h8v4a4 4 0 0 1-8 0zM6 9h2v2h2v2H4v-2h2z" fill="#fff"/></svg>Select League</span>
    </div>
    <div class="grid col-head">
      <div>Time</div><div>Event</div>
      <div class="ft"><div class="top">Full Time</div><div class="sub">A 1x2</div><div class="sub">HDP</div><div class="sub">OU</div><div class="sub">1x2</div></div>
      <div class="ft2"><div class="top">Full Time</div><div class="sub">HDP</div><div class="sub">OU</div><div class="sub">1x2</div></div>
      <div class="more">+ More</div>
    </div>
    <div class="league"><svg class="star" width="12" height="12"><use href="#i-star"/></svg>Southern Premier League<svg class="reload" width="12" height="12" style="color:#fff"><use href="#i-reload"/></svg></div>
    <div class="grid match alt short">
      <div class="c-stat"><svg width="12" height="12"><use href="#i-stat"/></svg></div>
      <div class="c-time">16:30<em>Live</em></div>
      <div class="c-event"><svg width="13" height="13"><use href="#i-star-o"/></svg><div class="teams"><div class="home">Harbour Coast Anchors</div><div class="away">Southbank Victors</div></div></div>
      <div class="c-a1x2"></div>
      <div class="c-hdp"><span class="line-val">0-0.5</span><div class="odds"><div class="pos">0.77</div><div class="neg">-0.95</div></div></div>
      <div class="c-ou"><span class="line-val">6-6.5</span><span class="ab">o<br>u</span><div class="odds"><div class="up">-0.85</div><div class="neg">0.65</div></div></div>
      <div class="c-1x2"></div><div class="c-ft2"></div>
      <div class="c-more"><svg width="8" height="14"><use href="#i-updown"/></svg>13</div>
    </div>
  </section>

  <section class="board" style="top:265px">
    <div class="board-title">
      <span class="title"><svg width="20" height="18" viewBox="0 0 20 18"><circle cx="12" cy="4" r="3" fill="#fff"/><path d="M4 16l5-6 4 2 3-3" stroke="#fff" stroke-width="2.4" fill="none"/></svg>Today - Live</span>
      <span class="count"><svg width="14" height="14" style="color:#fff"><use href="#i-reload"/></svg>38</span>
      <span class="league-pick"><svg width="14" height="14" viewBox="0 0 14 14"><path d="M3 1h8v4a4 4 0 0 1-8 0zM6 9h2v2h2v2H4v-2h2z" fill="#fff"/></svg>Select League</span>
    </div>
    <div class="grid col-head">
      <div>Time</div><div>Event</div>
      <div class="ft"><div class="top">Full Time</div><div class="sub">A 1x2</div><div class="sub">HDP</div><div class="sub">OU</div><div class="sub">1x2</div></div>
      <div class="ft2"><div class="top">Full Time</div><div class="sub">HDP</div><div class="sub">OU</div><div class="sub">1x2</div></div>
      <div class="more">+ More</div>
    </div>

    <div class="league"><svg class="star" width="12" height="12"><use href="#i-star"/></svg>Southern Premier League<svg class="reload" width="12" height="12" style="color:#fff"><use href="#i-reload"/></svg></div>
    <div class="grid match"><div class="c-stat"><svg width="12" height="12"><use href="#i-stat"/></svg></div><div class="c-time">16:30<em>Live</em></div><div class="c-event"><svg width="13" height="13"><use href="#i-star-o"/></svg><div class="teams"><div class="home">Harbour Coast Anchors</div><div class="away">Southbank Victors</div><div class="draw">Draw</div></div></div><div class="c-a1x2"></div><div class="c-hdp"><span class="line-val">0-0.5</span><div class="odds"><div class="pos">0.77</div><div class="neg">-0.95</div></div></div><div class="c-ou"><span class="line-val">6-6.5</span><span class="ab">o<br>u</span><div class="odds"><div class="neg">-0.85</div><div class="pos">0.65</div></div></div><div class="c-1x2"></div><div class="c-ft2"></div><div class="c-more"><svg width="8" height="14"><use href="#i-updown"/></svg>13</div></div>

    <div class="league"><svg class="star" width="12" height="12"><use href="#i-star"/></svg>Southern Premier League<svg class="reload" width="12" height="12" style="color:#fff"><use href="#i-reload"/></svg></div>
    <div class="grid match"><div class="c-stat"><svg width="12" height="12"><use href="#i-stat"/></svg></div><div class="c-time">16:30<em>Live</em></div><div class="c-event"><svg width="13" height="13"><use href="#i-star-o"/></svg><div class="teams"><div class="home">Harbour Coast Anchors</div><div class="away">Southbank Victors</div><div class="draw">Draw</div></div></div><div class="c-a1x2"></div><div class="c-hdp"><span class="line-val">0-0.5</span><div class="odds"><div class="pos">0.77</div><div class="neg">-0.95</div></div></div><div class="c-ou"><span class="line-val">6-6.5</span><span class="ab">o<br>u</span><div class="odds"><div class="neg">-0.85</div><div class="pos">0.65</div></div></div><div class="c-1x2"></div><div class="c-ft2"></div><div class="c-more"><svg width="8" height="14"><use href="#i-updown"/></svg>13</div></div>
    <div class="grid match alt"><div class="c-stat"><svg width="12" height="12"><use href="#i-stat"/></svg></div><div class="c-time">16:30<em>Live</em></div><div class="c-event"><svg width="13" height="13"><use href="#i-star-o"/></svg><div class="teams"><div class="home">Harbour Coast Anchors</div><div class="away">Southbank Victors</div><div class="draw">Draw</div></div></div><div class="c-a1x2"></div><div class="c-hdp"><span class="line-val">0-0.5</span><div class="odds"><div class="pos">0.77</div><div class="neg">-0.95</div></div></div><div class="c-ou"><span class="line-val">6-6.5</span><span class="ab">o<br>u</span><div class="odds"><div class="neg">-0.85</div><div class="pos">0.65</div></div></div><div class="c-1x2"></div><div class="c-ft2"></div><div class="c-more"><svg width="8" height="14"><use href="#i-updown"/></svg>13</div></div>
    <div class="grid match"><div class="c-stat"><svg width="12" height="12"><use href="#i-stat"/></svg></div><div class="c-time">16:30<em>Live</em></div><div class="c-event"><svg width="13" height="13"><use href="#i-star-o"/></svg><div class="teams"><div class="home">Harbour Coast Anchors</div><div class="away">Southbank Victors</div><div class="draw">Draw</div></div></div><div class="c-a1x2"></div><div class="c-hdp"><span class="line-val">0-0.5</span><div class="odds"><div class="pos">0.77</div><div class="neg">-0.95</div></div></div><div class="c-ou"><span class="line-val">6-6.5</span><span class="ab">o<br>u</span><div class="odds"><div class="neg">-0.85</div><div class="pos">0.65</div></div></div><div class="c-1x2"></div><div class="c-ft2"></div><div class="c-more"><svg width="8" height="14"><use href="#i-updown"/></svg>13</div></div>

    <div class="league"><svg class="star" width="12" height="12"><use href="#i-star"/></svg>Southern Premier League<svg class="reload" width="12" height="12" style="color:#fff"><use href="#i-reload"/></svg></div>
    <div class="grid match"><div class="c-stat"><svg width="12" height="12"><use href="#i-stat"/></svg></div><div class="c-time">16:30<em>Live</em></div><div class="c-event"><svg width="13" height="13"><use href="#i-star-o"/></svg><div class="teams"><div class="home">Harbour Coast Anchors</div><div class="away">Southbank Victors</div><div class="draw">Draw</div></div></div><div class="c-a1x2"></div><div class="c-hdp"><span class="line-val">0-0.5</span><div class="odds"><div class="pos">0.77</div><div class="neg">-0.95</div></div></div><div class="c-ou"><span class="line-val">6-6.5</span><span class="ab">o<br>u</span><div class="odds"><div class="neg">-0.85</div><div class="pos">0.65</div></div></div><div class="c-1x2"></div><div class="c-ft2"></div><div class="c-more"><svg width="8" height="14"><use href="#i-updown"/></svg>13</div></div>

    <div class="league"><svg class="star" width="12" height="12"><use href="#i-star"/></svg>Southern Premier League<svg class="reload" width="12" height="12" style="color:#fff"><use href="#i-reload"/></svg></div>
    <div class="grid match"><div class="c-stat"><svg width="12" height="12"><use href="#i-stat"/></svg></div><div class="c-time">16:30<em>Live</em></div><div class="c-event"><svg width="13" height="13"><use href="#i-star-o"/></svg><div class="teams"><div class="home">Harbour Coast Anchors</div><div class="away">Southbank Victors</div><div class="draw">Draw</div></div></div><div class="c-a1x2"></div><div class="c-hdp"><span class="line-val">0-0.5</span><div class="odds"><div class="pos">0.77</div><div class="neg">-0.95</div></div></div><div class="c-ou"><span class="line-val">6-6.5</span><span class="ab">o<br>u</span><div class="odds"><div class="neg">-0.85</div><div class="pos">0.65</div></div></div><div class="c-1x2"></div><div class="c-ft2"></div><div class="c-more"><svg width="8" height="14"><use href="#i-updown"/></svg>13</div></div>
    <div class="grid match alt"><div class="c-stat"><svg width="12" height="12"><use href="#i-stat"/></svg></div><div class="c-time">16:30<em>Live</em></div><div class="c-event"><svg width="13" height="13"><use href="#i-star-o"/></svg><div class="teams"><div class="home">Harbour Coast Anchors</div><div class="away">Southbank Victors</div><div class="draw">Draw</div></div></div><div class="c-a1x2"></div><div class="c-hdp"><span class="line-val">0-0.5</span><div class="odds"><div class="pos">0.77</div><div class="neg">-0.95</div></div></div><div class="c-ou"><span class="line-val">6-6.5</span><span class="ab">o<br>u</span><div class="odds"><div class="neg">-0.85</div><div class="pos">0.65</div></div></div><div class="c-1x2"></div><div class="c-ft2"></div><div class="c-more"><svg width="8" height="14"><use href="#i-updown"/></svg>13</div></div>
    <div class="grid match"><div class="c-stat"><svg width="12" height="12"><use href="#i-stat"/></svg></div><div class="c-time">16:30<em>Live</em></div><div class="c-event"><svg width="13" height="13"><use href="#i-star-o"/></svg><div class="teams"><div class="home">Harbour Coast Anchors</div><div class="away">Southbank Victors</div><div class="draw">Draw</div></div></div><div class="c-a1x2"></div><div class="c-hdp"><span class="line-val">0-0.5</span><div class="odds"><div class="pos">0.77</div><div class="neg">-0.95</div></div></div><div class="c-ou"><span class="line-val">6-6.5</span><span class="ab">o<br>u</span><div class="odds"><div class="neg">-0.85</div><div class="pos">0.65</div></div></div><div class="c-1x2"></div><div class="c-ft2"></div><div class="c-more"><svg width="8" height="14"><use href="#i-updown"/></svg>13</div></div>
    <div class="grid match alt"><div class="c-stat"><svg width="12" height="12"><use href="#i-stat"/></svg></div><div class="c-time">16:30<em>Live</em></div><div class="c-event"><svg width="13" height="13"><use href="#i-star-o"/></svg><div class="teams"><div class="home">Harbour Coast Anchors</div><div class="away">Southbank Victors</div><div class="draw">Draw</div></div></div><div class="c-a1x2"></div><div class="c-hdp"><span class="line-val">0-0.5</span><div class="odds"><div class="pos">0.77</div><div class="neg">-0.95</div></div></div><div class="c-ou"><span class="line-val">6-6.5</span><span class="ab">o<br>u</span><div class="odds"><div class="neg">-0.85</div><div class="pos">0.65</div></div></div><div class="c-1x2"></div><div class="c-ft2"></div><div class="c-more"><svg width="8" height="14"><use href="#i-updown"/></svg>13</div></div>
    <div class="grid match"><div class="c-stat"><svg width="12" height="12"><use href="#i-stat"/></svg></div><div class="c-time">16:30<em>Live</em></div><div class="c-event"><svg width="13" height="13"><use href="#i-star-o"/></svg><div class="teams"><div class="home">Harbour Coast Anchors</div><div class="away">Southbank Victors</div><div class="draw">Draw</div></div></div><div class="c-a1x2"></div><div class="c-hdp"><span class="line-val">0-0.5</span><div class="odds"><div class="pos">0.77</div><div class="neg">-0.95</div></div></div><div class="c-ou"><span class="line-val">6-6.5</span><span class="ab">o<br>u</span><div class="odds"><div class="neg">-0.85</div><div class="pos">0.65</div></div></div><div class="c-1x2"></div><div class="c-ft2"></div><div class="c-more"><svg width="8" height="14"><use href="#i-updown"/></svg>13</div></div>
    <div class="grid match alt"><div class="c-stat"><svg width="12" height="12"><use href="#i-stat"/></svg></div><div class="c-time">16:30<em>Live</em></div><div class="c-event"><svg width="13" height="13"><use href="#i-star-o"/></svg><div class="teams"><div class="home">Harbour Coast Anchors</div><div class="away">Southbank Victors</div><div class="draw">Draw</div></div></div><div class="c-a1x2"></div><div class="c-hdp"><span class="line-val">0-0.5</span><div class="odds"><div class="pos">0.77</div><div class="neg">-0.95</div></div></div><div class="c-ou"><span class="line-val">6-6.5</span><span class="ab">o<br>u</span><div class="odds"><div class="neg">-0.85</div><div class="pos">0.65</div></div></div><div class="c-1x2"></div><div class="c-ft2"></div><div class="c-more"><svg width="8" height="14"><use href="#i-updown"/></svg>13</div></div>
    <div class="grid match"><div class="c-stat"><svg width="12" height="12"><use href="#i-stat"/></svg></div><div class="c-time">16:30<em>Live</em></div><div class="c-event"><svg width="13" height="13"><use href="#i-star-o"/></svg><div class="teams"><div class="home">Harbour Coast Anchors</div><div class="away">Southbank Victors</div><div class="draw">Draw</div></div></div><div class="c-a1x2"></div><div class="c-hdp"><span class="line-val">0-0.5</span><div class="odds"><div class="pos">0.77</div><div class="neg">-0.95</div></div></div><div class="c-ou"><span class="line-val">6-6.5</span><span class="ab">o<br>u</span><div class="odds"><div class="neg">-0.85</div><div class="pos">0.65</div></div></div><div class="c-1x2"></div><div class="c-ft2"></div><div class="c-more"><svg width="8" height="14"><use href="#i-updown"/></svg>13</div></div>
    <div class="grid match alt"><div class="c-stat"><svg width="12" height="12"><use href="#i-stat"/></svg></div><div class="c-time">16:30<em>Live</em></div><div class="c-event"><svg width="13" height="13"><use href="#i-star-o"/></svg><div class="teams"><div class="home">Harbour Coast Anchors</div><div class="away">Southbank Victors</div><div class="draw">Draw</div></div></div><div class="c-a1x2"></div><div class="c-hdp"><span class="line-val">0-0.5</span><div class="odds"><div class="pos">0.77</div><div class="neg">-0.95</div></div></div><div class="c-ou"><span class="line-val">6-6.5</span><span class="ab">o<br>u</span><div class="odds"><div class="neg">-0.85</div><div class="pos">0.65</div></div></div><div class="c-1x2"></div><div class="c-ft2"></div><div class="c-more"><svg width="8" height="14"><use href="#i-updown"/></svg>13</div></div>
  </section>

  <footer class="footer">
    <span>Betting Rules</span><i>|</i><span>Contact Us</span><i>|</i><span>Privacy Policy</span><i>|</i><span>Responsible Gambling</span><i>|</i><span>Term &amp; Conditions</span><i>|</i><span>Tutorials</span>
  </footer>
</div>
</body>
</html>
```